Letterhead and Stationary for Construction Company

Brisk Current needs modern Letterhead, Envelopes and Notepad designs.

Industry/Entity Type

Construction

Colors
f78f20
34a7d8
ffffff

Requirements
Must have
• Modern looking design.

```html
<!DOCTYPE html>
<html lang="en">
<head>
<meta charset="utf-8">
<title>Brisk Current Letterhead</title>
<link href="https://fonts.googleapis.com/css2?family=Fira+Sans:wght@400;700&display=swap" rel="stylesheet">
<style>
  :root {
    --orange: #ec7211;
    --blue: #1a6fbd;
    --ink: #474747;
    --rule: #6b6b6b;
    --paper: #ffffff;
  }
  html, body {
    margin: 0;
    padding: 0;
    overflow: hidden;
    background: var(--paper);
  }
  .letterhead {
    position: relative;
    width: 851px;
    height: 1200px;
    background: var(--paper);
    overflow: hidden;
    font-family: "Fira Sans", sans-serif;
    color: var(--ink);
  }
  .brand-band {
    position: absolute;
    left: 0;
    top: 44px;
    width: 134px;
    height: 72px;
    background: var(--orange);
  }
  .brand-dot {
    position: absolute;
    left: 118px;
    top: 52px;
    width: 56px;
    height: 56px;
    border-radius: 50%;
    background: var(--orange);
    border: 4px solid var(--paper);
  }
  .brand-name {
    position: absolute;
    left: 190px;
    top: 60px;
    margin: 0;
    font-size: 34px;
    font-weight: 700;
    line-height: 1;
    color: var(--blue);
    letter-spacing: -0.5px;
  }
  .address {
    position: absolute;
    left: 473px;
    top: 72px;
    width: 168px;
    margin: 0;
    font-style: normal;
    font-size: 14px;
    line-height: 26px;
    white-space: nowrap;
  }
  .divider {
    position: absolute;
    left: 651px;
    top: 61px;
    width: 1px;
    height: 70px;
    background: var(--rule);
  }
  .contact-list {
    position: absolute;
    left: 664px;
    top: 55px;
    margin: 0;
    padding: 0;
    list-style: none;
    font-size: 14px;
    white-space: nowrap;
  }
  .contact-list li {
    display: flex;
    align-items: center;
    height: 25px;
  }
  .contact-icon {
    flex: none;
    width: 13px;
    height: 13px;
    margin-right: 9px;
    fill: none;
    stroke: var(--blue);
    stroke-width: 1.6;
  }
  .contact-icon.solid {
    fill: var(--blue);
    stroke: none;
  }
</style>
</head>
<body>
<main class="letterhead">
  <header class="masthead">
    <div class="brand-band"></div>
    <div class="brand-dot"></div>
    <h1 class="brand-name">Brisk Current</h1>

    <address class="address">
      218 Ridge Drive,Suite 14<br>
      Fairview, CA95021
    </address>

    <div class="divider"></div>

    <ul class="contact-list">
      <li>
        <svg class="contact-icon" viewBox="0 0 16 16" aria-hidden="true">
          <path d="M4 1.5l2.5 3-1.5 1.8c.8 1.8 2 3 3.8 3.8l1.8-1.5 3 2.5-1.6 2.4C7 13.5 2.5 9 1.6 3.1z"/>
          <path d="M9.5 2.5a4 4 0 0 1 4 4M9.5 5a1.5 1.5 0 0 1 1.5 1.5"/>
        </svg>
        (555)0142837
      </li>
      <li>
        <svg class="contact-icon solid" viewBox="0 0 16 16" aria-hidden="true">
          <path d="M1 3h14v10H1z"/>
          <path d="M1.5 3.5L8 9l6.5-5.5" fill="none" stroke="#fff" stroke-width="1.3"/>
        </svg>
        hello@briskcurrent.co
      </li>
      <li>
        <svg class="contact-icon solid" viewBox="0 0 16 16" aria-hidden="true">
          <circle cx="8" cy="8" r="7"/>
          <path d="M4 4.5c1.5.5 2 1.5 1.5 3s1 2 1 3.5M10 2.5c-.5 1.5.5 2.5 2 2.5M9.5 14c0-2 1-3 3-3.5" fill="none" stroke="#fff" stroke-width="1.2"/>
        </svg>
        www.briskcurrent.co
      </li>
    </ul>
  </header>
</main>
</body>
</html>
```